32 x 24 Swinging Real Estate Yard Sign

We are looking to design a new sign for our business to focus on the remodeling of homes to sell. We are looking to have a yard sign that gets peoples attention and is informational. The headline will be "The Secret to Top Dollar? Remodel First.". We remodel homes for sellers with no up front cost, as they simply pay at closing. This link has more info, https://brightkeelhomes.com/Remodel
The message we want to convey to those seeing the sign is we are a one stop shop, who can renovate your home and sell it for no stress. We are licensed real estate agents and licensed contractors.
Both of these license numbers and info need to be on the design:
CADRE #07264918
Contractors License #2851736
Email: info@brightkeelhomes.com
Phone: (408)555-0183
I'll attach a sample sign we have for our agents normally as well as all brand art work.
• Pantone Colors
o #172A41
Dark blue
o #4381B1
Medium blue
o #6FA6CC
Light blue
Target Market(s)
Residential Real Estate Sellers
Industry/Entity Type
Real Estate
Colors
Designer to choose colors to be used in the design.

```html
<!DOCTYPE html>
<html lang="en">
<head>
<meta charset="utf-8">
<title>Brightkeel Homes – Remodel First Yard Sign</title>
<link href="https://fonts.googleapis.com/css2?family=Montserrat:wght@500;600;700;800&display=swap" rel="stylesheet">
<style>
  :root {
    --navy: #172A41;
    --navy-deep: #111E30;
    --navy-light: #22395A;
    --blue-mid: #4381B1;
    --blue-light: #6FA6CC;
    --white: #FFFFFF;
    --backdrop: #E9ECF0;
  }
  * { margin: 0; padding: 0; box-sizing: border-box; }
  html, body {
    width: 1200px; height: 1002px; overflow: hidden;
    background: var(--backdrop);
    font-family: "Montserrat", sans-serif;
  }
  .yard-sign {
    position: absolute; left: 247px; top: 31px;
    width: 705px; height: 940px;
    background: radial-gradient(ellipse 75% 55% at 60% 28%, var(--navy-light) 0%, var(--navy) 70%);
    overflow: hidden;
    box-shadow: 0 8px 24px rgba(0,0,0,.18);
  }
  .licenses {
    position: absolute; left: 27px; top: 58px;
    color: var(--white); font-weight: 700; font-size: 13px; line-height: 17px;
  }
  .brand {
    position: absolute; right: 52px; top: 142px;
    display: flex; align-items: center; gap: 14px;
  }
  .brand-mark {
    width: 30px; height: 30px; border-radius: 50%;
    background: var(--white);
  }
  .brand-name {
    color: var(--white); font-weight: 600; font-size: 38px;
    letter-spacing: 1px; text-transform: uppercase; line-height: 1;
  }
  .kicker {
    position: absolute; left: 42px; top: 290px;
    color: var(--blue-light); font-weight: 800; font-size: 36px;
    line-height: 41px; letter-spacing: 2.5px; text-transform: uppercase;
  }
  .headline {
    position: absolute; left: 38px; top: 380px;
    color: var(--white); font-weight: 800; font-size: 122px;
    line-height: 112px; letter-spacing: -4px;
  }
  .headline .dot {
    display: inline-block; width: 26px; height: 26px; border-radius: 50%;
    background: var(--blue-mid); margin-left: 4px;
  }
  .offer {
    position: absolute; left: 46px; top: 626px;
    color: var(--white); font-weight: 500; font-size: 28px;
    line-height: 39px; letter-spacing: 1px;
  }
  .contact-band {
    position: absolute; left: 0; right: 0; bottom: 0; height: 188px;
    background: var(--navy-deep);
    border-radius: 44px 44px 0 0;
    text-align: center;
  }
  .phone {
    margin-top: 28px;
    color: var(--blue-light); font-weight: 700; font-size: 68px;
  }
  .email {
    margin-top: 4px;
    color: var(--white); font-weight: 500; font-size: 28px;
  }
</style>
</head>
<body>
  <section class="yard-sign">
    <p class="licenses">CADRE #07264918<br>Contractors License #2851736</p>

    <div class="brand">
      <span class="brand-mark" aria-hidden="true"></span>
      <p class="brand-name">Brightkeel Homes</p>
    </div>

    <h2 class="kicker">The Secret<br>to Top Dollar?</h2>

    <h1 class="headline">Remodel<br>First<span class="dot"></span></h1>

    <p class="offer">Get the best ROI for your<br>home with no upfront cost!</p>

    <footer class="contact-band">
      <p class="phone">(408)555-0183</p>
      <p class="email">info@brightkeelhomes.com</p>
    </footer>
  </section>
</body>
</html>
```